Lumora Flow Collective Business Cards

I need business cards for staff in a new startup. Our company name is MorvaLeap - we train Tai Chi teachers. But our biggest project is called Lumora Flow Collective - a federal project to put together free Tai Chi classes for Vets all across America. It's a young company, with a spirit of excitement, passion, a desire to do good for others (our Vets) and a modern style and sensibility. In other words, not old-fashioned Asian martial arts theme, but something new.

Industry/Entity Type

Health And Wellness

Contact Information for Business Card

The topic is ancient healing, but the company is the Quibbletons - so I'd like a card design that captures that.

Font styles to use
Sans Serif

Colors

Designer to choose colors to be used in the design.

Requirements
Nice to have
• I've got two logos - one for the company and one for the project. I want to see if we can incorporate them both without it becoming too busy.
Should not have
• Overly old-fashioned yin-yang themes.

```html
<!DOCTYPE html>
<html lang="en">
<head>
<meta charset="utf-8">
<title>MorvaLeap – Business Cards</title>
<link href="https://fonts.googleapis.com/css2?family=Lato:wght@400;700;900&display=swap" rel="stylesheet">
<style>
  :root {
    --stage: #2a2a2c;
    --card: #1c1d1f;
    --card-edge: #101112;
    --red: #d4202a;
    --red-deep: #8e0f14;
    --gold: #f0d75e;
    --text: #f2f2f2;
    --muted: #8a8a8a;
    --rule: #6a6a6a;
  }
  * { box-sizing: border-box; margin: 0; padding: 0; }
  html, body { width: 1200px; height: 1108px; overflow: hidden; }
  body {
    background: var(--stage);
    font-family: "Lato", sans-serif;
    display: flex;
    align-items: center;
    justify-content: center;
    gap: 60px;
  }
  .card {
    width: 500px;
    height: 820px;
    background: var(--card);
    border-radius: 26px;
    box-shadow: 0 18px 40px rgba(0,0,0,.45);
    position: relative;
    overflow: hidden;
  }
  /* front */
  .card--front { display: flex; flex-direction: column; align-items: center; }
  .brand {
    margin-top: 170px;
    display: flex; align-items: center; gap: 18px;
  }
  .brand__dot {
    width: 96px; height: 96px; border-radius: 50%;
    background: radial-gradient(circle at 40% 35%, var(--red), var(--red-deep));
  }
  .brand__name { font-size: 46px; font-weight: 700; color: var(--gold); }
  .person { margin-top: 150px; text-align: center; }
  .person__name { font-size: 30px; font-weight: 900; color: var(--red); letter-spacing: 1px; text-transform: uppercase; }
  .person__role { font-size: 22px; color: var(--text); margin-top: 2px; }
  .divider { display: flex; align-items: center; gap: 10px; margin-top: 22px; width: 300px; }
  .divider__line { flex: 1; height: 1px; background: var(--rule); }
  .divider__icons { display: flex; gap: 6px; }
  .icon { width: 30px; height: 30px; border-radius: 50%; background: var(--red); display: flex; align-items: center; justify-content: center; }
  .contact { margin-top: 16px; text-align: center; font-size: 22px; line-height: 1.3; color: var(--text); }
  .rule { width: 300px; height: 1px; background: var(--rule); margin: 16px 0; }
  .address { text-align: center; font-size: 22px; line-height: 1.3; color: var(--text); }
  /* back */
  .pattern {
    position: absolute; inset: 0;
    background: linear-gradient(160deg, #242527 0%, #1c1d1f 60%, #1a1b1d 100%);
  }
  .back__mark {
    position: absolute; right: 70px; top: 470px;
    display: flex; align-items: center; gap: 10px;
  }
  .back__mark-dot { width: 34px; height: 34px; border-radius: 50%; background: var(--gold); }
  .back__mark-name { font-size: 22px; font-weight: 700; color: var(--gold); }
  .project {
    position: absolute; left: 60px; bottom: 130px;
    display: flex; align-items: center; gap: 16px;
  }
  .project__ring { width: 74px; height: 74px; border-radius: 50%; border: 2px solid var(--text); }
  .project__name { font-size: 28px; font-weight: 400; color: var(--text); }
</style>
</head>
<body>
  <section class="card card--front">
    <div class="brand">
      <div class="brand__dot"></div>
      <div class="brand__name">MorvaLeap</div>
    </div>
    <div class="person">
      <div class="person__name">Dorian Vale</div>
      <div class="person__role">Managing Director</div>
    </div>
    <div class="divider">
      <span class="divider__line"></span>
      <div class="divider__icons">
        <span class="icon"><svg width="16" height="16" viewBox="0 0 16 16"><path d="M3 2h3l1 3-2 1a8 8 0 0 0 5 5l1-2 3 1v3c0 1-1 1-1 1A12 12 0 0 1 2 3s0-1 1-1z" fill="#1c1d1f"/></svg></span>
        <span class="icon"><svg width="16" height="16" viewBox="0 0 16 16"><rect x="2" y="4" width="12" height="8" fill="#1c1d1f"/><path d="M2 4l6 5 6-5" stroke="#d4202a" stroke-width="1.2" fill="none"/></svg></span>
        <span class="icon"><svg width="16" height="16" viewBox="0 0 16 16"><circle cx="8" cy="8" r="6" fill="none" stroke="#1c1d1f" stroke-width="1.5"/><path d="M2 8h12M8 2c-3 3-3 9 0 12M8 2c3 3 3 9 0 12" stroke="#1c1d1f" stroke-width="1.2" fill="none"/></svg></span>
      </div>
      <span class="divider__line"></span>
    </div>
    <div class="contact">
      <div>044-555 018 274</div>
      <div>info@morvaleap.com</div>
      <div>www.morvaleap.com</div>
    </div>
    <div class="rule"></div>
    <div class="address">
      <div>421, Address line here,</div>
      <div>45452, Country Name</div>
    </div>
  </section>

  <section class="card card--back">
    <div class="pattern" role="img" aria-label="Faint repeating brand mark pattern in dark grey"></div>
    <div class="back__mark">
      <span class="back__mark-dot"></span>
      <span class="back__mark-name">MorvaLeap</span>
    </div>
    <div class="project">
      <span class="project__ring"></span>
      <span class="project__name">Lumora Flow Collective</span>
    </div>
  </section>
</body>
</html>
```